Products & Services Postcard For our Vacuum Repair Store & Carpet Cleaning Company

SEE ATTACHED DOCUMENTS FOR FRONT AND BACK OF CARD.
Also, Brand logos are available in my attachments

We are a Retail Vacuum Repair shop and we also have Three carpet cleaning trucks that operate out of our location. In addition to servicing Vacuum Cleaners we also offer in home cleaning services that include: Carpet cleaning, upholstery cleaning, tile & Grout Cleaning, general cleaning services, move out clean ups, one time cleanings, post construction cleanup and strip & wax floorsWe Need to design a KTRW(nbfl kestrel lane route) postcard that shows and tells everything we do. Postcard should include all our services, have before and after pictures, list benefits of doing business with us and should have coupons attached to create urgency to call usWe:Fully Insured, commercial & Residential, free estimatesWe are the only Vacuum Store in area that is a Certified OTWAB Cleaner.Also, the only OTWAB Certified cleaner that services Vacuum Cleaners.We have a great reputation as a 5 Star Vacuum Service Station and Also a 5 Star Cleaning Company. We are a one stop shop for ALL your cleaning needs.Our goal is to educate customers and provide options.Goal of the card is to get customers to call or stop in for advice on both their vacuum cleaner and cleaning their homes. Goal is to get phone to ring or get people through the door.

Target Market(s)

Homeowners, People interested in clean

Colors

Designer to choose colors to be used in the design.

Requirements
Must have
• Before & After pics
• Coupons
• List of services
• Call to Action
• Address
• Phone #
Nice to have
• One side of postcard could be about our Vacuum Cleaner repair shop.
• The other side could be about our cleaning business

```html
<!DOCTYPE html>
<html lang="en">
<head>
<meta charset="utf-8">
<title>Harborline Vacuums Postcard</title>
<link rel="stylesheet" href="https://fonts.googleapis.com/css2?family=Cabin:ital,wght@0,400;0,500;0,600;0,700;1,400;1,500&family=Arimo:wght@400;700&display=swap">
<style>
:root{
  --navy:#1a3a5e;
  --navy-deep:#10294a;
  --green:#8db92e;
  --lime:#a3c93a;
  --sky:#5fb6e6;
  --white:#ffffff;
  --ink:#1b2f4b;
  --page:#f4f4f4;
  --photo-warm:#b9a88c;
}
*{box-sizing:border-box;margin:0;padding:0}
html,body{width:1200px;height:1000px;overflow:hidden}
body{background:var(--page);font-family:"Cabin",Arial,sans-serif;position:relative;color:var(--white)}
.card{position:absolute;left:265px;width:665px;overflow:hidden;background:var(--white)}
.card-front{top:15px;height:463px}
.card-back{top:512px;height:460px}
.abs{position:absolute}

/* FRONT */
.front-panel{left:0;top:0;width:665px;height:343px;background:var(--navy)}
.hero-photo{left:215px;top:0;width:450px;height:180px;background:linear-gradient(135deg,#d9d2c2,var(--photo-warm) 55%,#8d8270);clip-path:polygon(20px 0,450px 0,450px 180px,90px 180px)}
.brand{left:22px;top:58px;display:flex;align-items:center;gap:8px}
.brand-dot{width:14px;height:14px;border-radius:50%;background:var(--white)}
.brand-name{font-weight:700;font-size:19px;line-height:19px;letter-spacing:.5px;color:var(--white)}
.headline{left:23px;top:118px;font-weight:700;color:var(--lime);font-size:29px;line-height:31px}
.headline .small{font-size:22px;line-height:28px;display:block}
.subhead{left:23px;top:209px;font-size:18px;color:var(--sky)}
.service-list{list-style:none;font-size:12px;line-height:14px}
.service-list li{position:relative;padding-left:15px;margin-bottom:5px}
.service-list li::before{content:"";position:absolute;left:0;top:1px;width:10px;height:10px;border:1.3px solid var(--white);border-radius:50%}
.service-list li::after{content:"";position:absolute;left:3.5px;top:3px;width:3px;height:5px;border:solid var(--white);border-width:0 1.5px 1.5px 0;transform:rotate(40deg)}
.list-a{left:23px;top:246px}
.list-b{left:150px;top:246px}
.visit-strip{left:330px;top:180px;width:335px;height:38px;background:var(--navy-deep)}
.quote-band{left:290px;top:218px;width:375px;height:82px;background:var(--white)}
.tech-photo{left:278px;top:170px;width:64px;height:128px;background:linear-gradient(180deg,#c9a58a,#e06a2a 70%,#3b3b3b)}
.visit-text{left:347px;top:191px;font-size:9px;line-height:11px;font-weight:600;z-index:2}
.quote{left:400px;top:238px;font-style:italic;font-weight:500;font-size:12.5px;line-height:15px;color:var(--ink);text-align:center;width:150px}
.trained{left:356px;top:280px;font-weight:700;font-size:12.5px;color:var(--ink);z-index:2}
.before-photo{left:500px;top:114px;width:102px;height:64px;background:linear-gradient(135deg,#8b7f6d,#a89883);border:3px solid var(--white);transform:rotate(-3deg)}
.after-photo{left:556px;top:196px;width:100px;height:68px;background:linear-gradient(135deg,#b6a58e,#d3c5b0);border:3px solid var(--white);transform:rotate(8deg)}
.tag{font-weight:700;font-size:14px;color:var(--white);position:absolute;top:0;left:18px}
.call-strip{left:290px;top:300px;width:375px;height:43px;background:var(--navy-deep)}
.call-line{left:320px;top:304px;font-weight:600;font-size:17px;line-height:18px}
.call-line b{color:var(--lime)}
.call-sub{left:395px;top:325px;font-size:13px;font-weight:500}
.coupons{left:0;top:343px;width:665px;height:120px;background:var(--green);display:flex}
.coupon{height:100%;border-right:1.5px dashed var(--navy);color:var(--ink);text-align:center;padding-top:22px}
.coupon:last-child{border-right:none}
.c-label{font-size:11px;line-height:12px}
.c-label.tiny{font-size:8.5px;line-height:10px}
.c-price{font-size:46px;line-height:48px;font-weight:500;color:var(--navy)}
.c-note{font-size:8px}
.c-free{font-size:42px;line-height:40px;font-weight:500;color:var(--navy)}
.c-free-note{font-size:10.5px;line-height:12px;color:var(--white)}
.c-free-note .big{font-size:14px;line-height:15px}

/* BACK */
.back-panel{left:0;top:0;width:500px;height:296px;background:var(--navy)}
.back-photo{left:222px;top:0;width:278px;height:296px;background:linear-gradient(160deg,#3d4a5e,#8d9fb6 45%,#b7895a 80%,#a56f3e);clip-path:polygon(30px 0,278px 0,278px 296px,0 296px)}
.frustrated{left:20px;top:20px;font-size:19px;line-height:22px;color:var(--sky)}
.tune-band{left:0;top:68px;width:258px;height:55px;background:var(--green);clip-path:polygon(0 0,258px 0,240px 55px,0 55px)}
.tune-title{left:20px;top:70px;font-weight:700;font-size:26px;line-height:26px;color:var(--navy-deep)}
.offer-note{left:20px;top:127px;font-style:italic;font-size:8.5px}
.repair-intro{left:20px;top:148px;font-size:11px}
.repair-list{left:20px;top:167px;list-style:none;font-size:10.5px;line-height:12px}
.repair-list li{margin-bottom:6.5px;padding-left:13px;position:relative}
.repair-list li::before{content:"";position:absolute;left:1px;top:3px;width:5px;height:5px;border:solid var(--white);border-width:1.5px 1.5px 0 0;transform:rotate(45deg)}
.pull-note{left:20px;top:265px;font-style:italic;font-size:10px;line-height:12px}
.five-star{left:0;top:296px;width:500px;height:30px;background:var(--navy-deep);text-align:center;font-size:17px;line-height:30px;letter-spacing:.3px}
.brands-intro{left:0;top:334px;width:500px;text-align:center;font-size:10px;color:var(--ink)}
.brand-grid{left:15px;top:353px;width:475px;display:grid;grid-template-columns:repeat(5,1fr);row-gap:14px;font-family:"Arimo",Arial,sans-serif;font-weight:700;font-size:18px;color:var(--ink);text-align:center}
.bottom-call{left:0;top:420px;width:195px;height:40px;background:var(--green);clip-path:polygon(0 0,195px 0,180px 40px,0 40px);font-size:14px;line-height:40px;padding-left:10px;font-weight:500}
.bottom-call b{font-weight:700}
.bottom-addr{left:180px;top:420px;width:320px;height:40px;background:var(--navy-deep);clip-path:polygon(15px 0,320px 0,320px 40px,0 40px);font-size:10px;line-height:40px;padding-left:20px;white-space:nowrap}
.bottom-addr i{font-size:7.5px}
.mail-side{left:500px;top:0;width:165px;height:460px;background:var(--white);border-left:1px solid #ddd}
.indicia{left:571px;top:16px;width:82px;height:80px;border:1px solid #333;font-family:"Arimo",Arial,sans-serif;font-size:10.5px;line-height:13px;color:#111;text-align:center;padding-top:6px}
.address-box{left:527px;top:105px;width:124px;height:42px;border:1px solid #333;font-family:"Arimo",Arial,sans-serif;font-size:6px;line-height:8px;color:#222;padding:12px 0 0 8px}
.back-brand{left:520px;top:408px;display:flex;align-items:center;gap:7px}
.back-brand .brand-dot{background:var(--ink)}
.back-brand .brand-name{color:var(--ink);font-size:18px}
</style>
</head>
<body>

<section class="card card-front">
  <div class="abs front-panel"></div>
  <div class="abs hero-photo" role="img" aria-label="Photo of a carpet cleaning wand extracting dirt from a sofa cushion"></div>

  <div class="abs brand"><span class="brand-dot"></span><span class="brand-name">HARBORLINE<br>VACUUMS</span></div>

  <h1 class="abs headline">CARPETS<br>&amp; FLOORING<span class="small">NEED CLEANING?</span></h1>
  <p class="abs subhead">Furniture Need Cleaning?</p>

  <ul class="abs service-list list-a">
    <li>Commercial</li>
    <li>Residential</li>
    <li>General Cleaning</li>
    <li>Move In &amp;<br>Move Out Cleanings</li>
  </ul>
  <ul class="abs service-list list-b">
    <li>Carpet Cleaning</li>
    <li>Tile &amp; Grout Cleaning</li>
    <li>VCT Strip &amp; Wax</li>
    <li>Furniture Cleaning</li>
  </ul>

  <div class="abs visit-strip"></div>
  <div class="abs quote-band"></div>
  <div class="abs tech-photo" role="img" aria-label="Photo of a smiling cleaning technician in an orange safety vest"></div>
  <p class="abs visit-text">Visit HarborlineVacuums.com and get your FREE<br>Report on <i>"How To Choose A Cleaning Company"</i></p>
  <p class="abs quote">"Nobody Does It Better<br>&amp; Gives You More"</p>
  <p class="abs trained">Friendly, Professional, OTWAB Trained Technicians</p>

  <div class="abs before-photo" role="img" aria-label="Before photo of a stained carpet"><span class="tag">Before</span></div>
  <div class="abs after-photo" role="img" aria-label="After photo of a freshly cleaned carpet"><span class="tag">After</span></div>

  <div class="abs call-strip"></div>
  <p class="abs call-line">Call <b>555-014-2290</b> for a FREE Estimates</p>
  <p class="abs call-sub">on ALL Your Cleaning Needs!</p>

  <div class="abs coupons">
    <div class="coupon" style="width:133px">
      <p class="c-label tiny">Whole House Carpet Cleaning<br>Up To 700 Sq Ft ONLY</p>
      <p class="c-price">$189</p>
    </div>
    <div class="coupon" style="width:132px">
      <p class="c-label" style="font-size:12px">Furniture Cleaning<br><span style="font-size:9px">(Sofa, Loveseat &amp; Chair)</span></p>
      <p class="c-price">$199</p>
    </div>
    <div class="coupon" style="width:135px">
      <p class="c-label">Tile &amp; Grout Cleaning<br>Kitchen Floor Only</p>
      <p class="c-price">$119</p>
      <p class="c-note">(Up To 120 Sq Ft)</p>
    </div>
    <div class="coupon" style="width:130px;padding-top:20px">
      <p class="c-free">FREE</p>
      <p class="c-free-note" style="color:var(--ink)">Cleaning Kit(Value of $59)<br>for Your Carpet When<br><span class="big">You Add Protector</span></p>
    </div>
    <div class="coupon" style="width:135px;padding-top:20px">
      <p class="c-free">FREE</p>
      <p class="c-free-note">Tile &amp; Grout Cleaning Kit<br><span class="big">(Value of $59)</span><br>When you Add Sealer</p>
    </div>
  </div>
</section>

<section class="card card-back">
  <div class="abs back-panel"></div>
  <div class="abs back-photo" role="img" aria-label="Photo of a technician opening a canister vacuum on a wood floor"></div>

  <p class="abs frustrated">Are You Frustrated With Your<br>Vacuum Cleaner?!</p>
  <div class="abs tune-band"></div>
  <h2 class="abs tune-title">VACUUM TUNE UP<br>FOR ONLY $19.99</h2>
  <p class="abs offer-note">*Offer Expires in 30 days &nbsp;&nbsp; **Limit One Vacuum Per Coupon</p>

  <p class="abs repair-intro">Our Repair Center Offers:</p>
  <ul class="abs repair-list">
    <li>Free Estimates</li>
    <li>Experienced &amp; Trained Technicians</li>
    <li>Fast, reliable service</li>
    <li>Courtesy (loaner vacuums)</li>
    <li>Drive Up (Curbside Service)</li>
  </ul>
  <p class="abs pull-note">Pull in, honk, call or blink your<br>lights and we'll carry the vacuum in for you!</p>

  <p class="abs five-star">FIVE STAR VACUUM CLEANER REPAIR SHOP</p>
  <p class="abs brands-intro">We Service All Makes &amp; Models Including:</p>
  <div class="abs brand-grid">
    <span>TORVA</span><span>BRENLO</span><span>KALDER</span><span>Vinto</span><span>Homewell</span>
    <span>Skipjack</span><span>Aerolux</span><span>Plainline</span><span>Arcbow</span><span>fenwick</span>
  </div>

  <p class="abs bottom-call">CALL NOW! <b>555-014-2290</b></p>
  <p class="abs bottom-addr">2847 Elm Ave Millbrook (Eastvale), NY 10990 <i>*Just off 9 Exit 4E</i></p>

  <div class="abs mail-side"></div>
  <div class="abs indicia">PRSRT STD<br>ECRWSS<br>U.S.POSTAGE<br><b>PAID</b><br>KTRW RETAIL</div>
  <div class="abs address-box">Local<br>Postal Customer</div>
  <div class="abs back-brand"><span class="brand-dot"></span><span class="brand-name">HARBORLINE<br>VACUUMS</span></div>
</section>

</body>
</html>
```